Design a Bold Tradeshow Backdrop for a Sustainable Cleaning Technology

We need a professional, high-impact 10' × 8' tradeshow backdrop for Vornelle®, a commercial cleaning technology company. 143.75" x 90" high and needs bleeds in the 143.75" direction for printing but the graphic area is 10' wide.

Our first event will have an audience that includes K–12 school administrators, facility managers, business officials, and custodial decision-makers. However, this backdrop will be used at multiple future trade shows across different commercial and institutional markets.

The design therefore needs to be universal rather than specifically education- or school-themed.

Our goal is to stop attendees as they walk past the booth and immediately communicate a simple message:

Safer and more sustainable cleaning can also cost substantially less than conventional cleaning chemicals.

We want the design to feel modern, innovative, clean, sustainable, credible, commercial, and premium. It should resonate with K–12 decision-makers while being equally appropriate at events serving commercial facilities, healthcare, hospitality, government, property management, transportation, and other institutional markets.

It should NOT look like a traditional janitorial supply advertisement and should not be overly busy.

The most important messages need to be understandable from approximately 10–20 feet away.

Required Messaging

The primary headline should be:

SUSTAINABLE CLEANING
DOES NOT HAVE TO BE EXPENSIVE.

Three major value propositions should be prominently displayed:

FREE
Cleaning Chemical Analysis
See how much you can save.

SAVE UP TO 60% or More
on Cleaning Chemical Costs

AS LITTLE AS $0.27/GALLON

We would also like a strong secondary message incorporated into the design:

SMARTER CLEANING.
High Performance. Low Cost. Safer.

Visual Direction — Important

Rather than showing a K–12 school hallway or other environment that limits the backdrop to the education market, we want a sophisticated, universal commercial or institutional environment.

This could be a bright, contemporary commercial facility, lobby, corridor, office environment, public building, or other premium architectural space that could reasonably represent many different types of facilities.

The environment should communicate:

Cleanliness • Safety • Sustainability • Professionalism • Efficiency • High Performance

We want someone from a school, hospital, hotel, office building, airport, government facility, or other commercial property to be able to look at the backdrop and relate the imagery to their own facility.

Please avoid imagery that makes the backdrop industry-specific.

We also want to avoid clichéd environmental imagery. The design does not need to be covered in leaves, trees, water droplets, recycling symbols, or other obvious "green" graphics to communicate sustainability. We prefer a sophisticated commercial interpretation of sustainability.

Color & Brand Direction

We want the overall color palette to stay primarily within:

Blues — consistent with our corporate identity

Greens — to reinforce sustainability, safety, efficiency, and environmental responsibility

White — strongly encouraged for clean space, contrast, and an open contemporary appearance

Black — should be limited primarily to text where necessary for readability

Please avoid making black a major background or dominant design color.

We want the finished display to have a bright, clean, sophisticated, sustainable look and feel rather than a dark or industrial appearance.

The design should use significant negative space and a strong visual hierarchy.

Less is more.

We prefer a few large, powerful messages that can be understood quickly rather than numerous small bullet points, paragraphs, or icons.

Creative Freedom

The attached concept image is provided to communicate our general direction and messaging only.

It does not need to be copied.

We are specifically running this contest because we want designers to improve upon our initial concept and show us different creative approaches to presenting the Vornelle value proposition.

We are open to creative interpretations of the commercial environment, composition, typography, use of negative space, and how the three major financial benefits are presented.

The finished design should feel like an innovative commercial technology brand, not simply another cleaning chemical company.

Corporate Logo — Very Important

We are attaching our official Vornelle® corporate logo for use in the design.

DO NOT redraw, recreate, modify, stylize, reinterpret, trace, or AI-generate the Vornelle logo.

The supplied corporate logo must be inserted directly into the artwork exactly as provided, maintaining its original proportions, colors, typography, trademark elements, and graphic design.

The logo should generally appear in the upper-left area of the backdrop but should not overwhelm the primary marketing message.

Printer Template & Graphic Sizing

We are also attaching the printer's official graphic template and instructions for the 8' × 8' tension-fabric display.

Designers should create their artwork using these supplied specifications so the winning design can be transferred directly into production.

The printer requires that the original document size not be changed, artwork be created on the designated design layer or a new layer, images be embedded, text be converted to outlines, and the finished production artwork be supplied as a PDF.

Please pay particular attention to the bleed area, finished size, and safe artwork area when positioning important text, graphics, and the corporate logo.

Physical Booth Context

The backdrop will sit behind an 8' tradeshow table.

The complete booth will also contain:

A blue stretch tablecloth with the Vornelle corporate logo
BrevoMax and Vornelle product containers and samples on the table
An HulaDrent chemical mixing/dilution station displayed on an elevated stand to the left
A television/monitor to the right demonstrating our online ROI cost-savings calculator

Because these other booth elements will explain our products and technology in greater detail, the backdrop should NOT attempt to explain everything we do.

Its primary purpose is to stop traffic, establish the Vornelle brand, and communicate our core economic and sustainability value proposition.

Final Deliverables

The winning designer must provide artwork properly sized and positioned using our supplied 8' × 8' tension-fabric display template.

Final files should include:

Print-ready, high-resolution PDF
Editable source/vector artwork
All images embedded
Fonts converted to outlines
Artwork correctly positioned within the supplied printer template
Original Vornelle corporate logo incorporated without modification
The 3–5 Second Test

This is perhaps the most important requirement.

Someone walking down a tradeshow aisle should be able to look at the backdrop for 3–5 seconds and understand:

Vornelle offers safer, sustainable, high-performance commercial cleaning — at a lower cost.

The three offers we particularly want them to remember are:

FREE CHEMICAL ANALYSIS

SAVE UP TO 60%

AS LITTLE AS $0.27/GALLON

The overall takeaway should be:

Sustainable cleaning does not have to cost more.

We want the winning design to make that message immediately understandable, credible, and memorable.

Colors
0054AA
0677BA
7BADD7
CADEEF
E8F1F8
0094D4
00A9DD
6FCCEA
C7EBF8
E9F6FB
00AB8E
00BBA5
67D7C9
C6EFE9
E9F9F6
59FF00
82FF00
B8FF75
E3FFCB
F4FFEA

```html
<!DOCTYPE html>
<html lang="en">
<head>
<meta charset="utf-8">
<title>Vornelle — Sustainable Cleaning</title>
<link rel="stylesheet" href="https://fonts.googleapis.com/css2?family=Bebas+Neue&family=Montserrat:wght@800&family=Questrial&display=swap">
<style>
  :root {
    --navy: #22377a;
    --blue-text: #2e86c8;
    --band-teal: #1f8fa5;
    --card-teal: #0aaba5;
    --arc-dark: #1652a0;
    --arc-light: #c6dff4;
    --arc-pale: #e3eef8;
    --panel: #e5eef8;
    --white: #ffffff;
  }
  * { margin: 0; padding: 0; box-sizing: border-box; }
  html, body { width: 1200px; height: 1200px; overflow: hidden; background: var(--white); }
  .canvas { position: relative; width: 1200px; height: 1200px; overflow: hidden; background: var(--white); }
  .arcs { position: absolute; inset: 0; }
  .brand-panel {
    position: absolute; left: 0; top: 0; width: 482px; height: 222px;
    background: var(--panel); border-bottom-right-radius: 90px;
  }
  .brand-name {
    position: absolute; left: 48px; top: 76px;
    font-family: "Montserrat", sans-serif; font-weight: 800; font-size: 62px;
    color: var(--navy); line-height: 1; letter-spacing: -1px; white-space: nowrap;
  }
  .display { font-family: "Bebas Neue", sans-serif; line-height: 1; position: absolute; white-space: nowrap; }
  .headline { color: var(--navy); font-size: 167px; left: 44px; letter-spacing: 0; }
  .headline-1 { top: 253px; }
  .headline-2 { top: 384px; }
  .headline-rule { position: absolute; left: 47px; top: 541px; width: 706px; height: 11px; background: var(--band-teal); }
  .subhead { color: var(--blue-text); font-size: 64px; left: 47px; top: 566px; letter-spacing: 0.6px; }
  .smart-band { position: absolute; left: 0; top: 638px; width: 810px; height: 128px; }
  .smart-title {
    position: absolute; left: 84px; top: 651px; font-family: "Montserrat", sans-serif; font-weight: 800;
    font-size: 56px; color: var(--white); line-height: 1; white-space: nowrap;
  }
  .smart-sub {
    position: absolute; left: 90px; top: 715px; font-family: "Questrial", sans-serif;
    font-size: 31px; color: var(--white); line-height: 1; white-space: nowrap;
  }
  .offer {
    position: absolute; top: 800px; width: 318px; height: 400px;
    background: var(--card-teal); border-radius: 38px 38px 0 0;
  }
  .offer-free { left: 85px; }
  .offer-save { left: 441px; }
  .offer-price { left: 797px; }
  .offer .display { left: 0; width: 100%; text-align: center; }
  .navy { color: var(--navy); }
  .light { color: var(--white); }
  .free-word { font-size: 178px; top: 36px; letter-spacing: 2px; }
  .offer .free-note { font-size: 28px; top: 196px; left: 23px; text-align: left; line-height: 0.95; }
  .save-1 { font-size: 168px; top: 28px; }
  .save-2 { font-size: 155px; top: 158px; }
  .save-3 { font-size: 60px; top: 292px; }
  .price-1 { font-size: 76px; top: 23px; }
  .price-2 { font-size: 290px; top: 64px; }
  .price-3 { font-size: 56px; top: 310px; }
</style>
</head>
<body>
<main class="canvas">
  <svg class="arcs" width="1200" height="1200" viewBox="0 0 1200 1200" aria-hidden="true">
    <defs>
      <clipPath id="upper-area"><rect x="0" y="0" width="1200" height="792"/></clipPath>
    </defs>
    <g clip-path="url(#upper-area)">
      <circle cx="1560" cy="628" r="805" fill="var(--arc-pale)"/>
      <circle cx="1560" cy="628" r="741" fill="var(--arc-light)"/>
      <circle cx="1560" cy="628" r="688" fill="var(--arc-dark)"/>
      <circle cx="1560" cy="628" r="627" fill="var(--card-teal)"/>
      <circle cx="1562" cy="624" r="622" fill="var(--white)"/>
    </g>
    <polygon points="1122,1048 1200,1092 1200,1118 1122,1076" fill="var(--card-teal)"/>
    <polygon points="1122,1076 1200,1118 1200,1200 1168,1200 1122,1150" fill="var(--arc-dark)"/>
  </svg>

  <div class="brand-panel"></div>
  <p class="brand-name">Vornelle®</p>

  <h1>
    <span class="display headline headline-1">SUSTAINABLE</span>
    <span class="display headline headline-2">CLEANING</span>
  </h1>
  <div class="headline-rule"></div>
  <p class="display subhead">DOES NOT HAVE TO BE EXPENSIVE.</p>

  <svg class="smart-band" width="810" height="128" viewBox="0 0 810 128" aria-hidden="true">
    <polygon points="0,0 735,0 806,127 0,127" fill="var(--band-teal)"/>
    <polyline points="28,30 56,62 28,94" fill="none" stroke="var(--white)" stroke-width="3"/>
    <polyline points="46,30 74,62 46,94" fill="none" stroke="var(--white)" stroke-width="3"/>
  </svg>
  <p class="smart-title">SMARTER CLEANING.</p>
  <p class="smart-sub">High Performance. Low Cost. Safer.</p>

  <section class="offer offer-free">
    <span class="display navy free-word">FREE</span>
    <span class="display light free-note">CLEANING CHEMICAL ANALYSIS<br>SEE HOW MUCH YOU CAN SAVE.</span>
  </section>
  <section class="offer offer-save">
    <span class="display navy save-1">SAVE</span>
    <span class="display navy save-2">UP TO</span>
    <span class="display light save-3">60% OR MORE</span>
  </section>
  <section class="offer offer-price">
    <span class="display navy price-1">AS LITTLE</span>
    <span class="display navy price-2">AS</span>
    <span class="display light price-3">$0.27/GALLON</span>
  </section>
</main>
</body>
</html>
```